依頼詳細
基本構成については
https://zubira.com/diagrams/KtwrpLo39NzxQeYd/B71F4
上記をご確認ください。

導線や機能についてはtenpolyのデモページ
http://demoline.shop3.tenpoly.jp/
を参考にしております。
上記の機能範囲であれば、
自由にご提案いただいても問題ありません。

文言やレイアウト、順序などの構成については、
上記を基本としますが、自由にご提案頂いて構いません。
テキストや要素の追加、レイアウトの変更など歓迎いたします。
当方、jqueryなどを使用したコーディングも対応可能ですので、
そのようなご提案も歓迎いたします。

既存サイト
http://www.orbit-runa.jp/

ミルキーモールサイト
https://store.milkymall.jp/store-orbitruna/

上記をもとに、
デザインいただければ幸甚です。

・ロゴで使用している赤
・既存サイトのベースとなっているブルー
などをベースカラーとして頂ければ幸甚です。

テキスト・構成などについては、必要に応じて変更、添削頂いて結構です。
また素材については、ロゴと外観は添付いたしますが、
画像など、必要に応じてご用意いただけますと大変ありがたく存じます。
その際
http://gazolo.jp/
などの素材購入サイトから、
10000円程度までならこちらにて購入可能です。
カンプデータにて作成頂き、
納品時に当方にて購入したデータに差し替えていただければと存じます。

また、
既存サイト

ミルキーモールサイト
で使用している画像については、
自由に引用頂いて構いません。
サイトURL
ページ数
1ページ
希望イメージ
シンプル 複雑
単色 カラフル
暗い 明るい
日常 高級
遊び心 厳粛
未来的 伝統的
女性的 男性的
希望する色
赤系、青系
納品ファイル
• 高解像度JPG (.jpg)
• フォトショップ形式 (.psd)
補足説明
基本構成については
上記をご確認ください。

納品ファイルはフォトショップのほかXDでのご提出でも構いません。

また、添付ファイル以外
http://gazolo.jp/
などから、10000円程度までならこちらにて購入可能です。
カンプデータにて作成頂き、
納品時に購入したデータに差し替えていただければと存じます。

・見やすく探しやすい、視認性の高いデザイン
・ブルー、レッドなどを使ったスポーティな印象

を与えられればと考えております。

制作にあたりご不明な点がございましたら、
お気軽にお申し付けいただければと存じます。
よろしくお願いいたします。

クライアント様との協議の結果こちらの案を採用させていただきました。

この度は多数ご提案いただきありがとうございました。
当選に至らなかったクエスター様におかれましては大変心苦しいのですが、
またの機会にぜひご提案いただければ幸甚です。
引き続き何卒よろしくお願いいたします。

```html
<!DOCTYPE html>
<html lang="ja">
<head>
<meta charset="utf-8">
<title>KAZAMI TACKLE | 湖畔のバスフィッシング専門店</title>
<link href="https://fonts.googleapis.com/css2?family=Noto+Sans+JP:wght@400;500;700&family=Roboto:ital,wght@0,400;0,700;1,700;1,900&display=swap" rel="stylesheet">
<style>
:root{
  --navy:#1b2a48;
  --navy-deep:#141f36;
  --blue:#2a5d9c;
  --red:#d4242b;
  --bg:#e3e8ee;
  --white:#ffffff;
  --text:#2b2f36;
  --muted:#7b8594;
  --line:#d5dbe3;
}
*{box-sizing:border-box;margin:0;padding:0}
html,body{width:1200px;height:2816px;overflow:hidden}
body{position:relative;background:var(--bg);font-family:"Noto Sans JP",sans-serif;color:var(--text);font-size:12px}
.en{font-family:"Roboto",sans-serif}
ul{list-style:none}

.topbar{position:absolute;top:0;left:0;width:1200px;height:32px;background:var(--navy-deep);color:#cfd6e2;font-size:10px;display:flex;align-items:center;justify-content:space-between;padding:0 120px}
.topbar .notes span{margin-right:18px}
.topbar .notes b{color:#fff}
.cards{display:flex;gap:4px}
.cards i{display:block;width:26px;height:16px;background:#fff;border-radius:2px}

.header{position:absolute;top:32px;left:0;width:1200px;height:88px;background:var(--white);display:flex;align-items:center;justify-content:space-between;padding:0 120px}
.brand{display:flex;align-items:center;gap:10px}
.brand .dot{width:30px;height:30px;border-radius:50%;background:var(--red)}
.brand .name{font-family:"Roboto",sans-serif;font-weight:700;font-size:24px;color:var(--navy);letter-spacing:2px;white-space:nowrap}
.brand .sub{font-size:10px;color:var(--muted);margin-top:2px}
.tel{text-align:right}
.tel .num{display:flex;align-items:center;gap:8px;font-family:"Roboto",sans-serif;font-weight:700;font-size:30px;color:var(--navy)}
.tel .hours{font-size:10px;color:var(--muted)}

.nav{position:absolute;top:120px;left:0;width:1200px;height:40px;background:var(--navy);display:flex;align-items:center;justify-content:space-between;padding:0 120px;color:#fff;font-size:12px}
.nav .menu{display:flex;gap:26px}
.nav .acts{display:flex;gap:8px;height:40px;align-items:center}
.nav .acts a{display:flex;align-items:center;gap:6px;padding:0 16px;height:28px;color:#fff;text-decoration:none;font-size:11px}
.nav .acts .cart{background:var(--red);height:40px}

.hero{position:absolute;top:160px;left:120px;width:960px;height:580px;background:linear-gradient(160deg,#c9d3dd 0%,#8e9caa 45%,#4d5b6c 100%)}
.hero-panel{position:absolute;top:20px;left:30px;width:400px;height:440px;background:rgba(20,31,54,.92);color:#fff;padding:48px 36px}
.hero-panel h1{font-size:28px;line-height:1.5;font-weight:700;margin-bottom:24px;white-space:nowrap}
.hero-panel p{font-size:12px;line-height:2;color:#d9dfea}
.hero-panel .mark{position:absolute;left:36px;bottom:36px;display:flex;align-items:center;gap:10px;background:#fff;padding:8px 14px}
.hero-panel .mark i{width:22px;height:22px;border-radius:50%;background:var(--navy)}
.hero-panel .mark span{font-family:"Roboto",sans-serif;font-weight:700;color:var(--navy);font-size:13px;letter-spacing:1px;white-space:nowrap}

.side{position:absolute;top:780px;left:128px;width:252px}
.box{background:var(--white);padding:18px 18px 20px;margin-bottom:24px}
.box-title{font-family:"Roboto",sans-serif;font-style:italic;font-weight:900;color:var(--navy);font-size:16px;text-align:center}
.box-title small{display:block;font-family:"Noto Sans JP",sans-serif;font-style:normal;font-weight:400;font-size:9px;color:var(--muted);margin-top:2px}
.search{display:flex;margin-top:14px}
.search span{flex:1;height:30px;border:1px solid var(--line)}
.search b{width:30px;height:30px;background:var(--navy);display:flex;align-items:center;justify-content:center}
.cat{margin-top:14px}
.cat li{font-size:11px;line-height:22px;border-bottom:1px dotted var(--line);padding-left:12px;position:relative}
.cat li::before{content:"";position:absolute;left:0;top:9px;width:4px;height:4px;background:var(--red)}
.blog{height:130px;background:linear-gradient(135deg,#5b6e82,#2c3a4c);display:flex;align-items:center;justify-content:center;color:#fff;font-weight:700;font-size:22px;letter-spacing:4px}

.main{position:absolute;top:780px;left:420px;width:660px}
.sec{background:var(--white);padding:20px 22px 24px;margin-bottom:24px}
.sec-title{display:flex;align-items:baseline;gap:10px;border-bottom:2px solid var(--navy);padding-bottom:8px;margin-bottom:14px}
.sec-title h2{font-family:"Roboto",sans-serif;font-style:italic;font-weight:900;font-size:22px;color:var(--navy)}
.sec-title small{font-size:10px;color:var(--muted)}
.info li{display:flex;gap:24px;font-size:11px;line-height:34px;border-bottom:1px dotted var(--line)}
.info time{color:var(--muted);font-family:"Roboto",sans-serif}
.info a{color:var(--blue);text-decoration:none}

.products{display:grid;grid-template-columns:repeat(5,1fr);gap:10px}
.product .pic{height:116px;border:1px solid var(--line);background:linear-gradient(160deg,#f3f5f8,#c8d0da)}
.product p{font-size:10px;line-height:1.5;margin-top:8px;height:45px;overflow:hidden}
.product .price{color:var(--red);font-weight:700;font-size:12px;font-family:"Roboto",sans-serif}
.product .price small{font-size:9px;color:var(--muted);font-weight:400}

.tiles{display:grid;grid-template-columns:repeat(5,1fr);gap:14px 10px}
.tile .pic{height:150px;background:linear-gradient(160deg,#6d7d8f,#24324a)}
.tile.alt .pic{background:linear-gradient(160deg,#d9e0e8,#8797a8)}
.tile .label{height:28px;background:var(--navy);color:#fff;font-size:11px;display:flex;align-items:center;justify-content:center}

.scenery{position:absolute;top:2200px;left:0;width:1200px;height:440px;background:linear-gradient(180deg,#dfe7ef 0%,#b9c8d6 35%,#8497aa 60%,#3c4a58 100%)}

.footer{position:absolute;top:2640px;left:0;width:1200px;height:176px;background:var(--navy-deep);color:#c8d0dc}
.footer .inner{position:absolute;top:38px;left:120px;width:960px;display:flex;justify-content:space-between;align-items:center}
.footer .brand .name{color:#fff;font-size:22px}
.footer .links{display:flex;gap:28px;font-size:12px;color:#fff}
.footer .bottom{position:absolute;top:128px;left:120px;width:960px;display:flex;justify-content:space-between;font-size:10px;border-top:1px solid #2d3a55;padding-top:14px}
</style>
</head>
<body>

<div class="topbar">
  <div class="notes"><span><b>送料無料！</b>20,000円以上のご注文で送料無料</span><span>平日15時までのご注文で当日発送</span><span>20,000円以上で代引手数料無料</span></div>
  <div class="cards"><i></i><i></i><i></i><i></i><i></i></div>
</div>

<header class="header">
  <div class="brand">
    <div class="dot"></div>
    <div><div class="name">KAZAMI TACKLE</div><div class="sub">LAKE BASS FISHING SHOP</div></div>
  </div>
  <div class="tel">
    <div class="num">
      <svg width="22" height="22" viewBox="0 0 24 24"><path fill="#1b2a48" d="M6.6 10.8a15.1 15.1 0 0 0 6.6 6.6l2.2-2.2a1 1 0 0 1 1-.25 11.4 11.4 0 0 0 3.6.57 1 1 0 0 1 1 1V20a1 1 0 0 1-1 1A17 17 0 0 1 3 4a1 1 0 0 1 1-1h3.5a1 1 0 0 1 1 1c0 1.250.2 2.450.57 3.57a1 1 0 0 1-.25 1z"/></svg>
      0555-48-7712
    </div>
    <div class="hours">営業時間 10:00〜19:00（水曜定休）</div>
  </div>
</header>

<nav class="nav">
  <ul class="menu"><li>トップページ</li><li>新品一覧</li><li>店舗案内</li><li>ご利用ガイド</li><li>お問い合わせ</li></ul>
  <div class="acts">
    <a href="#">ログイン</a>
    <a href="#">マイページ</a>
    <a href="#" class="cart">
      <svg width="16" height="16" viewBox="0 0 24 24"><path fill="#fff" d="M7 18a2 2 0 1 0 0 4 2 2 0 0 0 0-4zm10 0a2 2 0 1 0 0 4 2 2 0 0 0 0-4zM5.2 4H2V2h4.6l.9 2H22l-3.4 8H8.4l-.9 2H20v2H4.3l2.2-4.4z"/></svg>
      カートを見る</a>
  </div>
</nav>

<section class="hero" role="img" aria-label="湖畔に建つ木造の店舗外観と青空の写真">
  <div class="hero-panel">
    <h1>山中湖湖畔の<br>バスフィッシング専門店</h1>
    <p>ロッド、リールからルアー、ボート用品、ウエアー等の釣具販売、エレクトロニクスの取り付けまで、湖畔のフィッシングショップとしてお客様の釣りをサポートいたします。</p>
    <div class="mark"><i></i><span>KAZAMI TACKLE</span></div>
  </div>
</section>

<aside class="side">
  <div class="box">
    <div class="box-title">Search</div>
    <div class="search"><span></span><b><svg width="14" height="14" viewBox="0 0 24 24"><circle cx="10" cy="10" r="6.5" fill="none" stroke="#fff" stroke-width="2.5"/><path d="M15 15l6 6" stroke="#fff" stroke-width="2.5"/></svg></b></div>
  </div>
  <div class="box">
    <div class="box-title">Item Search<small>アイテムから探す</small></div>
    <ul class="cat">
      <li>ロッド</li><li>リール</li><li>ハードベイト</li><li>ソフトベイト</li><li>ワーム</li><li>ラバージグ、その他ジグ</li><li>ボートアクセ</li><li>ジグ用ヘッド</li><li>ライン</li><li>フック、シンカー</li><li>アクセサリー</li><li>ボート備品</li><li>エレクトロニクス</li><li>魚群探知機関連</li><li>ウエア、キャップ</li><li>バッグ</li><li>DVD</li><li>雑貨グッズ</li><li>特価商品</li>
    </ul>
  </div>
  <div class="box">
    <div class="box-title">Maker Search<small>メーカーから探す</small></div>
    <ul class="cat">
      <li>ミナトロッド</li><li>アオバリール</li><li>コハクルアー</li><li>NAMIWORKS</li><li>ツバサ工房</li><li>ハヤテ</li><li>セキレイ</li><li>フカミ</li><li>シオカゼ</li><li>ソナリス</li><li>ミズホ</li><li>カゲロウ</li><li>ユウナギ</li><li>トキワ</li><li>アサギ</li><li>リンドウ</li><li>ハルカゼ</li><li>ヒバリ</li><li>その他メーカー</li>
    </ul>
  </div>
  <div class="blog" role="img" aria-label="湖面と釣り人のシルエットのブログ用バナー写真">店長ブログ</div>
</aside>

<main class="main">
  <section class="sec">
    <div class="sec-title"><h2>Information</h2><small>お知らせ</small></div>
    <ul class="info">
      <li><time>2020.01.01</time><a href="#">この文章はダミーです。新商品の入荷情報をお知らせします。</a></li>
      <li><time>2020.01.01</time><a href="#">年末年始の営業日についてのお知らせを掲載しました。</a></li>
      <li><time>2020.01.01</time><a href="#">この文章はダミーです。店頭イベントの日程を更新しました。</a></li>
    </ul>
  </section>

  <section class="sec">
    <div class="sec-title"><h2>Pickup Item</h2><small>ピックアップアイテム</small></div>
    <div class="products">
      <div class="product"><div class="pic" role="img" aria-label="スピニングリールの商品写真"></div><p>ミナトロッド スピニング 2500 ハイギア</p><div class="price">6,980円<small>(税込)</small></div></div>
      <div class="product"><div class="pic" role="img" aria-label="ベイトリールの商品写真"></div><p>アオバリール ベイトモデル 70HG 右巻き</p><div class="price">24,180円<small>(税込)</small></div></div>
      <div class="product"><div class="pic" role="img" aria-label="魚群探知機の商品写真"></div><p>ソナリス 魚群探知機 9インチ 振動子付き</p><div class="price">149,800円<small>(税込)</small></div></div>
      <div class="product"><div class="pic" role="img" aria-label="魚群探知機ディスプレイの商品写真"></div><p>ソナリス 魚群探知機 7インチ 本体のみ</p><div class="price">98,000円<small>(税込)</small></div></div>
      <div class="product"><div class="pic" role="img" aria-label="釣り糸スプールの商品写真"></div><p>フカミ フロロカーボン ライン 100m</p><div class="price">1,980円<small>(税込)</small></div></div>
    </div>
  </section>

  <section class="sec">
    <div class="sec-title"><h2>Item Search</h2><small>アイテムから探す</small></div>
    <div class="tiles">
      <div class="tile"><div class="pic" role="img" aria-label="ロッドの写真"></div><div class="label">ロッド</div></div>
      <div class="tile"><div class="pic" role="img" aria-label="リールの写真"></div><div class="label">リール</div></div>
      <div class="tile alt"><div class="pic" role="img" aria-label="ハードベイトの写真"></div><div class="label">ハードベイト</div></div>
      <div class="tile alt"><div class="pic" role="img" aria-label="ソフトベイトの写真"></div><div class="label">ソフトベイト</div></div>
      <div class="tile"><div class="pic" role="img" aria-label="ワームの写真"></div><div class="label">ワーム</div></div>
      <div class="tile alt"><div class="pic" role="img" aria-label="ラバージグの写真"></div><div class="label">ラバージグ</div></div>
      <div class="tile alt"><div class="pic" role="img" aria-label="シンカーの写真"></div><div class="label">シンカー</div></div>
      <div class="tile"><div class="pic" role="img" aria-label="フックの写真"></div><div class="label">フック</div></div>
      <div class="tile"><div class="pic" role="img" aria-label="アクセサリーの写真"></div><div class="label">アクセサリー</div></div>
      <div class="tile alt"><div class="pic" role="img" aria-label="ボート備品の写真"></div><div class="label">ボート備品</div></div>
      <div class="tile alt"><div class="pic" role="img" aria-label="ラインの写真"></div><div class="label">ライン</div></div>
      <div class="tile"><div class="pic" role="img" aria-label="バッグの写真"></div><div class="label">バッグ</div></div>
      <div class="tile"><div class="pic" role="img" aria-label="エレキモーターの写真"></div><div class="label">エレクトリック</div></div>
      <div class="tile"><div class="pic" role="img" aria-label="魚群探知機の写真"></div><div class="label">魚群探知機</div></div>
      <div class="tile alt"><div class="pic" role="img" aria-label="ウエアとキャップの写真"></div><div class="label">ウエア</div></div>
    </div>
  </section>
</main>

<div class="scenery" role="img" aria-label="雪山を背景に湖で釣りをする人物の風景写真"></div>

<footer class="footer">
  <div class="inner">
    <div class="brand">
      <div class="dot"></div>
      <div><div class="name">KAZAMI TACKLE</div><div class="sub">LAKE BASS FISHING SHOP</div></div>
    </div>
    <ul class="links"><li>個人情報保護ポリシー</li><li>特定商取引法表記</li><li>ご利用ガイド</li></ul>
  </div>
  <div class="bottom">
    <span>〒401-0000　山梨県みずうみ市湖畔町1-2-3</span>
    <span class="en">Copyright © KAZAMI TACKLE Co.,Ltd. All rights reserved.</span>
  </div>
</footer>

</body>
</html>
```